Brightmere Glowworks - Two Pages of Information and Pictures

We need a two page summary of the Service Offerings of Brightmere Glowworks - a company that installs LED Lighting. We've written the copy and picked images and chart that we like and have laid it out a word document.

We're looking for someone to design a more professional page layout than the generic Word Template. Please do not feel the current layout is suggested. It is only laid out this way because Word had that template. Be as creative as you want.

We would like the images and text to be in the same order that it is in now.

We're also in a rush so speed is appreciated. THANK YOU !!

Target Market(s)

Corporate Offices in New York

Industry/Entity Type

Lighting Fixture

Colors
85cae6
87cfc7
9bcb3c
3377b5

Requirements
Must have
• Must include two pages of the copy and images written and provided in the word document that was uploaded. Must use the Brightmere colors in the logo.
Nice to have
• An easy to read flow of images and.

```html
<!DOCTYPE html>
<html lang="en">
<head>
<meta charset="utf-8">
<title>Brightmere Glowworks – Two Page Summary</title>
<link rel="stylesheet" href="https://fonts.googleapis.com/css2?family=Montserrat:wght@400;500;600;700;800;900&family=Oswald:wght@500;600;700&family=Raleway:wght@300;400&display=swap">
<style>
:root{
  --blue-deep:#0d3f99;
  --blue:#1750b5;
  --blue-bright:#1c5fd0;
  --green:#9bcb3c;
  --green-dark:#7db52a;
  --sky:#85cae6;
  --teal:#87cfc7;
  --ink:#222;
  --grey-text:#444;
  --paper:#f2f2f2;
  --canvas:#e9e9e9;
}
*{margin:0;padding:0;box-sizing:border-box}
html,body{width:1200px;height:817px;overflow:hidden;background:var(--canvas)}
.stage{position:relative;width:1500px;height:1021px;transform:scale(.8);transform-origin:0 0;font-family:"Montserrat",sans-serif}
.page{position:absolute;top:85px;width:605px;height:845px;overflow:hidden;box-shadow:0 6px 18px rgba(0,0,0,.25)}
.page--front{left:116px;background:var(--blue)}
.page--back{left:769px;background:linear-gradient(180deg,#fafafa,#ececec)}
.page svg.bg{position:absolute;inset:0}
.abs{position:absolute}

/* front */
.brand-name{left:132px;width:340px;top:342px;text-align:center;font-family:"Raleway",sans-serif;font-weight:400;font-size:21px;letter-spacing:.5px;color:#4d7f6a}
.tagline{left:112px;width:380px;top:425px;text-align:center;font-family:"Raleway",sans-serif;font-size:14px;color:#333}
.headline{left:0;width:605px;top:565px;text-align:center;font-family:"Oswald",sans-serif;font-weight:700;font-size:40px;line-height:44px;transform:scaleX(.86)}
.headline .line1{color:#e4e4e4;display:block}
.headline .line2{color:var(--green);display:block}
.front-copy{left:74px;width:457px;top:672px;text-align:center;color:#fff;font-size:9.1px;line-height:15px}

.slogan{left:0;width:605px;top:771px;text-align:center;font-weight:800;font-size:24px;letter-spacing:3px;color:#111}
.contact{left:0;width:605px;top:811px;height:18px;display:flex;justify-content:center;align-items:center;gap:14px;color:#fff;font-size:9.6px;font-weight:600}
.contact span{display:flex;align-items:center;gap:6px}
.contact svg{width:12px;height:12px}

/* back */
.title{left:0;width:605px;top:74px;text-align:center;font-family:"Oswald",sans-serif;font-weight:700;font-size:36px;color:var(--green);transform:scaleX(.86)}
.logo-name{left:237px;width:120px;top:39px;text-align:center;font-size:6.5px;color:#5a7f6a;letter-spacing:.5px}
.section-head{left:0;padding-left:14px;border-left:5px solid var(--blue);font-weight:700;font-size:13px;color:var(--blue);line-height:14px}
.body{color:var(--grey-text);font-size:8.7px;line-height:12.6px;text-align:justify}
.body p+p{margin-top:12px}
.chart{left:316px;top:138px;width:262px;height:170px;background:#fff;border:1px solid #ddd}
.team-photo{left:320px;top:370px;width:270px;height:157px;background:linear-gradient(135deg,#5b7c48 0%,#4e6da8 45%,#3a5d9e 70%,#6c8b5a 100%)}
.quote{left:14px;width:576px;border:1px solid #bbb;background:rgba(255,255,255,.35);text-align:center;font-size:9.6px;line-height:13px;color:#333}
.quote b{display:block;color:var(--blue);font-size:10px;font-weight:700}
.quote-mark{font-family:"Oswald",sans-serif;font-weight:700;font-size:78px;color:#777;line-height:1}
</style>
</head>
<body>
<div class="stage">

  <!-- FRONT PAGE -->
  <section class="page page--front">
    <svg class="bg" width="605" height="845" viewBox="0 0 605 845">
      <defs>
        <linearGradient id="showroom" x1="0" y1="0" x2="0" y2="1">
          <stop offset="0" stop-color="#3a2a1c"/><stop offset=".5" stop-color="#a07a50"/><stop offset="1" stop-color="#6e4d30"/>
        </linearGradient>
        <linearGradient id="bulbs" x1="0" y1="0" x2="1" y2="1">
          <stop offset="0" stop-color="#d8c3a0"/><stop offset=".5" stop-color="#8a6040"/><stop offset="1" stop-color="#3a2a20"/>
        </linearGradient>
        <linearGradient id="office" x1="0" y1="0" x2="1" y2="1">
          <stop offset="0" stop-color="#eaeaea"/><stop offset=".6" stop-color="#b0b0b0"/><stop offset="1" stop-color="#6a6a6a"/>
        </linearGradient>
        <radialGradient id="blueglow" cx=".5" cy=".75" r=".7">
          <stop offset="0" stop-color="#1d5ec9"/><stop offset="1" stop-color="#0d3f99"/>
        </radialGradient>
      </defs>
      <rect width="605" height="845" fill="url(#blueglow)"/>
      <polygon points="0,0 605,0 605,205 490,320 302,185 115,320 0,205" fill="url(#showroom)" role="img" aria-label="Photo of a wood-panel showroom lit by track lights"/>
      <polygon points="0,215 190,395 0,580" fill="url(#bulbs)" role="img" aria-label="Photo of hanging Edison-style filament bulbs"/>
      <polygon points="605,200 405,395 605,590" fill="url(#office)" role="img" aria-label="Photo of an open-plan office with LED lighting"/>
      <polygon points="0,215 190,395 0,580" fill="none" stroke="#fff" stroke-width="3"/>
      <polygon points="605,200 405,395 605,590" fill="none" stroke="#fff" stroke-width="3"/>
      <polygon points="0,200 36,236 0,272" fill="var(--blue)"/>
      <polygon points="605,230 575,260 605,290" fill="var(--blue)"/>
      <polygon points="0,540 60,600 0,660" fill="var(--green)"/>
      <polygon points="605,540 548,598 605,656" fill="var(--green)"/>
      <polygon points="302,188 497,378 302,568 107,378" fill="#fafafa"/>
      <polygon points="302,205 478,378 302,551 126,378" fill="none" stroke="var(--green)" stroke-width="2.5"/>
      <polygon points="80,808 108,763 498,763 526,808" fill="var(--green)"/>
      <rect x="0" y="808" width="605" height="24" fill="var(--blue-bright)"/>
      <rect x="0" y="832" width="605" height="13" fill="var(--green)"/>
    </svg>
    <div class="abs brand-name">Brightmere Glowworks</div>
    <div class="abs tagline">Making light brilliant.</div>
    <h1 class="abs headline"><span class="line1">NO UPFRONT COST</span><span class="line2">TURNKEY LEDS</span></h1>
    <p class="abs front-copy">Brightmere Glowworks provides LED lighting as a service – fully implemented and managed LEDs at no upfront cost. Brightmere takes the risk, hassle and capital cost out of adopting LED's energy saving technology. Brightmere guarantees net-savings for customers on day one, and continues to guarantee savings and performance for the full term of the contract. And the savings add up! A project can be installed 2-4 weeks from kickoff, and projects continue to generate savings for up to 10 years.</p>
    <div class="abs slogan">MAKING LIGHT BRILLIANT</div>
    <div class="abs contact">
      <span><svg viewBox="0 0 12 12"><rect x="1" y="2.5" width="10" height="7" fill="none" stroke="#fff" stroke-width="1.2"/><path d="M1 2.5l5 4 5-4" fill="none" stroke="#fff" stroke-width="1.2"/></svg>CUSTOMERS@BRIGHTMEREGLOWWORKS.COM</span>
      <span><svg viewBox="0 0 12 12"><path d="M3 1l2 2.5-1.2 1.3a7 7 0 0 0 3.4 3.4L8.5 7 11 9l-1.5 2C5 11 1 7 1 2.5z" fill="#fff"/></svg>347 555 GLOW</span>
      <span><svg viewBox="0 0 12 12"><circle cx="6" cy="6" r="5" fill="none" stroke="#fff" stroke-width="1.1"/><ellipse cx="6" cy="6" rx="2.2" ry="5" fill="none" stroke="#fff" stroke-width="1"/><path d="M1 6h10" stroke="#fff" stroke-width="1"/></svg>BRIGHTMEREGLOWWORKS.COM</span>
    </div>
  </section>

  <!-- BACK PAGE -->
  <section class="page page--back">
    <svg class="bg" width="605" height="845" viewBox="0 0 605 845">
      <rect width="605" height="118" fill="var(--blue)"/>
      <polygon points="0,112 230,48 364,48 605,112 605,120 0,120" fill="#fafafa"/>
      <polygon points="0,104 230,40 364,40 605,104 605,112 364,48 230,48 0,112" fill="#6a8fd4" opacity=".5"/>
      <polygon points="297,5 365,43 297,80 229,43" fill="#fff"/>
      <polygon points="297,14 350,43 297,71 244,43" fill="none" stroke="var(--green)" stroke-width="2.5"/>
      <polygon points="80,808 108,763 498,763 526,808" fill="var(--green)"/>
      <rect x="0" y="808" width="605" height="24" fill="var(--blue-bright)"/>
      <rect x="0" y="832" width="605" height="13" fill="var(--green)"/>
    </svg>
    <div class="abs logo-name">BRIGHTMERE</div>
    <h1 class="abs title">BRIGHTMERE GLOWWORKS</h1>

    <h2 class="abs section-head" style="top:135px">WHY USE BRIGHTMERE?</h2>
    <div class="abs body" style="left:14px;width:284px;top:153px">
      <p>Brightmere's customers understand the value of LEDs but don't want to deal with the risk, hassle and capital cost on their own. Brightmere starts saving customers money the first month – typically a net-savings of about 4.7 cents a square-foot per month. Brightmere will design aesthetic LED systems and install the best available technology.</p>
      <p>Brightmere provides LEDs at the best cost with its as-a-service structure, which puts the cost of lighting into clients' monthly operating budget for less than they save. By installing projects immediately, Brightmere eliminates the cost of foregone savings that would accumulate from delayed implementation.</p>
    </div>

    <div class="abs chart">
      <svg width="262" height="170" viewBox="0 0 262 170" font-family="Montserrat,sans-serif">
        <text x="131" y="12" text-anchor="middle" font-size="7.5" fill="#333">Annual and Total Net-Savings of 250,000 ft2 Customer</text>
        <g font-size="4" fill="#555" text-anchor="end">
          <text x="28" y="24">$300</text><text x="28" y="44">$250</text><text x="28" y="64">$200</text><text x="28" y="84">$150</text><text x="28" y="104">$100</text><text x="28" y="124">$50</text><text x="28" y="143">$-</text>
        </g>
        <g font-size="4" fill="#555">
          <text x="246" y="24">$2.0</text><text x="246" y="48">$1.6</text><text x="246" y="72">$1.2</text><text x="246" y="96">$0.8</text><text x="246" y="120">$0.4</text><text x="246" y="143">$0.0</text>
        </g>
        <line x1="32" y1="141" x2="240" y2="141" stroke="#bbb" stroke-width=".6"/>
        <g fill="var(--sky)">
          <rect x="37" y="102" width="5" height="39"/><rect x="59" y="102" width="5" height="39"/><rect x="81" y="102" width="5" height="39"/><rect x="103" y="102" width="5" height="39"/><rect x="125" y="102" width="5" height="39"/>
        </g>
        <g fill="#7fbf5e">
          <rect x="43" y="85" width="6" height="56"/><rect x="65" y="85" width="6" height="56"/><rect x="87" y="85" width="6" height="56"/><rect x="109" y="85" width="6" height="56"/><rect x="131" y="85" width="6" height="56"/>
          <rect x="153" y="46" width="6" height="95"/><rect x="175" y="46" width="6" height="95"/><rect x="197" y="46" width="6" height="95"/><rect x="219" y="46" width="6" height="95"/>
        </g>
        <polyline points="40,140 62,136 84,130 106,124 128,115 150,102 172,88 194,74 216,55 230,30" fill="none" stroke="#8a8a8a" stroke-width="1"/>
        <g font-size="4" fill="#555" text-anchor="middle">
          <text x="43" y="149">1</text><text x="65" y="149">2</text><text x="87" y="149">3</text><text x="109" y="149">4</text><text x="131" y="149">5</text><text x="153" y="149">6</text><text x="175" y="149">7</text><text x="197" y="149">8</text><text x="219" y="149">9</text><text x="232" y="149">10</text>
        </g>
        <g font-size="3.6" fill="#555">
          <rect x="46" y="158" width="8" height="2" fill="var(--sky)"/><text x="56" y="160.5">Annual Brightmere Service</text>
          <rect x="120" y="158" width="8" height="2" fill="#7fbf5e"/><text x="130" y="160.5">Annual Net-Savings</text>
          <rect x="180" y="158.5" width="8" height="1" fill="#8a8a8a"/><text x="190" y="160.5">Total Net-Savings</text>
        </g>
      </svg>
    </div>

    <p class="abs body" style="left:14px;width:576px;top:316px">It can be risky to adopt new technology, especially when salespeople try to sell more than is needed. Brightmere has access to better equipment and at better cost than is widely available on the open market and passes that quality and savings on to its customers. Brightmere guarantees performance for 5 years, which removes the risk of a failed project.</p>

    <h2 class="abs section-head" style="top:367px">THE BEST TEAM IN LEDS</h2>
    <p class="abs body" style="left:14px;width:282px;top:390px">Brightmere is a team of lighting experts who get the evolution of lighting and efficiency. Simply put, we come in up every day with one goal: to provide an excellent service that saves money and uses less electricity. Part of the team focuses on the supply chain of the very best equipment that customers have come to appreciate. Part of the team focuses on the project management of each installation. And, part of the team focuses on resolving any questions customers might have in their transition. Together we make up the best team in LEDs and work tirelessly to make it easy to upgrade.</p>
    <div class="abs team-photo" role="img" aria-label="Photo of team members in matching blue shirts, seen from behind, among garden plants"></div>

    <h2 class="abs section-head" style="top:534px">TESTIMONIALS</h2>
    <div class="abs quote" style="top:563px;height:57px;padding:10px 50px 0 60px">“ Brightmere made a huge improvement in the lighting for our headquarters.<br>The installation process was as smooth as can be and the service since has been excellent.”<b>HARBORLINE HEALTH</b></div>
    <div class="abs quote-mark" style="left:20px;top:548px">“</div>
    <div class="abs quote" style="top:628px;height:56px;padding:10px 24px 0">“ In a museum, quality lighting is paramount. Brightmere has been a great partner in helping us transition to LEDs that look great, save us money, and make lighting management so much simpler. ”<b>MUSEUM OF YOUNG MINDS, NEW YORK</b></div>
    <div class="abs quote" style="top:692px;height:60px;padding:6px 20px 0">“ We are so happy to have had Brightmere's help building out our new office space – they put their lighting expertise to work delivering beautiful LEDs and fixtures. It was cost-effective, removed lighting from the build-out budget, and it's been a joy to work with them since.”<b>LATTICEWORKS, INC</b></div>
    <div class="abs quote-mark" style="left:536px;top:728px">”</div>

    <div class="abs slogan">MAKING LIGHT BRILLIANT</div>
    <div class="abs contact">
      <span><svg viewBox="0 0 12 12"><rect x="1" y="2.5" width="10" height="7" fill="none" stroke="#fff" stroke-width="1.2"/><path d="M1 2.5l5 4 5-4" fill="none" stroke="#fff" stroke-width="1.2"/></svg>CUSTOMERS@BRIGHTMEREGLOWWORKS.COM</span>
      <span><svg viewBox="0 0 12 12"><path d="M3 1l2 2.5-1.2 1.3a7 7 0 0 0 3.4 3.4L8.5 7 11 9l-1.5 2C5 11 1 7 1 2.5z" fill="#fff"/></svg>347 555 GLOW</span>
      <span><svg viewBox="0 0 12 12"><circle cx="6" cy="6" r="5" fill="none" stroke="#fff" stroke-width="1.1"/><ellipse cx="6" cy="6" rx="2.2" ry="5" fill="none" stroke="#fff" stroke-width="1"/><path d="M1 6h10" stroke="#fff" stroke-width="1"/></svg>BRIGHTMEREGLOWWORKS.COM</span>
    </div>
  </section>

</div>
</body>
</html>
```